Business card design for a dynamic IT consulting company

We need a business card design for a young firm, specialized in the Telecommunications/Consulting industry. The name of the company is Dulmar and Partners Business Consulting Ltd. (Short name: Dulmar and Partnes)
Dulmar = solve read reverse, so we aim to be uncomplicated and solution-oriented. The small pipe in our logo is also related to the word solve. So we need a new business card design, which is simple, eye catching and something non traditional (I would probably prefer a square shaped design rather than a rectangle, but open for suggestions). Attached our logo.

Target Market(s)

Usually our customers are Tier1 Telecoms providers (Q-Linkor, Teravine, etc) and their executives.

Industry/Entity Type

Business

Contact Information for Business Card

Name: Gergely Tarnavedi
Email: g.tarnavedi@dulmar-example.hu
Web: www.dulmar-example.hu
Mobile: +36 30 555 0192
Title: Managing Director

Optional:
Company name: Dulmar and Partners Ltd.
Address: 1021 Budapest, Kovarhegyi str. 17/B, Hungary

Font styles to use
Other font styles liked:
• helveticaneue_medium, Prime Regular are used now.

Colors

Designer to choose colors to be used in the design.

Requirements
Must have
• I would like to have a 2 sided design.
Nice to have
• I thought if we make the logo a bit bigger (without the company name), that could go to the back with the company name below. I though, if the pipe in the logo is somehow touchable on the business card, would be nice and unique.

```html
<!DOCTYPE html>
<html lang="en">
<head>
<meta charset="utf-8">
<title>Dulmar and Partners – Business Card</title>
<link rel="stylesheet" href="https://fonts.googleapis.com/css2?family=Maven+Pro:wght@500;600&family=Roboto:wght@400&display=swap">
<style>
  :root {
    --paper: #ffffff;
    --frame: #3a3a3a;
    --edge: #8a8a8a;
    --ink: #4b4b4d;
    --band: #4a4a4c;
    --band-text: #e3e3e3;
    --magenta: #b5318f;
    --cyan: #0b9ad6;
    --note: #7d7d7d;
  }
  html, body {
    margin: 0;
    padding: 0;
    width: 1200px;
    height: 1200px;
    overflow: hidden;
    background: var(--paper);
  }
  .sheet {
    position: relative;
    width: 1200px;
    height: 1200px;
    box-sizing: border-box;
    border: 2px solid var(--frame);
    background: var(--paper);
    font-family: "Maven Pro", sans-serif;
    color: var(--ink);
  }
  .card {
    position: absolute;
    left: 151px;
    width: 898px;
    height: 450px;
    box-sizing: border-box;
    border: 1px solid var(--edge);
    background: var(--paper);
    overflow: hidden;
  }
  .card--front { top: 112px; }
  .card--back  { top: 638px; }
  .card__band {
    position: absolute;
    left: 0;
    right: 0;
    bottom: 0;
    height: 186px;
    background: var(--band);
    color: var(--band-text);
    text-align: center;
  }

  /* Front */
  .wordmark {
    position: absolute;
    left: 0;
    right: 0;
    top: 115px;
    display: flex;
    justify-content: center;
    align-items: center;
    gap: 22px;
  }
  .wordmark__square {
    width: 26px;
    height: 26px;
    background: var(--magenta);
  }
  .wordmark__name {
    font-size: 66px;
    font-weight: 500;
    color: var(--ink);
    letter-spacing: 0.5px;
    line-height: 1;
  }
  .company {
    margin: 62px 0 0;
    font-size: 36px;
    font-weight: 600;
    letter-spacing: 0.5px;
    line-height: 1;
  }
  .address {
    margin: 12px 0 0;
    font-size: 17px;
    font-weight: 500;
    word-spacing: 4px;
    letter-spacing: 0.3px;
  }

  /* Back */
  .signature {
    position: absolute;
    left: 150px;
    top: 130px;
    display: flex;
    align-items: center;
    gap: 14px;
  }
  .signature__square {
    width: 22px;
    height: 22px;
    background: var(--cyan);
  }
  .signature__name {
    font-size: 40px;
    font-weight: 500;
    color: var(--ink);
    line-height: 1;
  }
  .contact {
    position: absolute;
    left: 370px;
    top: 78px;
    margin: 0;
    font-style: normal;
    color: var(--ink);
  }
  .contact__name {
    font-size: 30px;
    font-weight: 500;
    letter-spacing: 1.5px;
    word-spacing: 8px;
    line-height: 1.1;
  }
  .contact__title {
    font-size: 25px;
    font-weight: 500;
    letter-spacing: 3px;
    word-spacing: 6px;
    line-height: 1.25;
  }
  .contact__line {
    font-size: 24px;
    font-weight: 500;
    letter-spacing: 0.8px;
    line-height: 1.3;
  }
  .web {
    margin: 78px 0 0;
    font-size: 28px;
    font-weight: 500;
    letter-spacing: 0.5px;
    line-height: 1;
  }

  /* Presentation notes */
  .note-side {
    position: absolute;
    left: 1137px;
    top: 1090px;
    transform: rotate(-90deg);
    transform-origin: left top;
    font-family: "Roboto", sans-serif;
    font-size: 30px;
    color: var(--note);
    white-space: nowrap;
  }
  .note-size {
    position: absolute;
    left: 0;
    right: 0;
    top: 1136px;
    text-align: center;
    font-family: "Roboto", sans-serif;
    font-size: 17px;
    color: var(--note);
  }
</style>
</head>
<body>
<main class="sheet">

  <section class="card card--front" aria-label="Card front">
    <div class="wordmark">
      <span class="wordmark__square" aria-hidden="true"></span>
      <span class="wordmark__name">Dulmar &amp; Partners</span>
    </div>
    <div class="card__band">
      <p class="company">Dulmar and Partners Ltd.</p>
      <p class="address">1021 Budapest, Kovarhegyi str. 17/B, Hungary</p>
    </div>
  </section>

  <section class="card card--back" aria-label="Card back">
    <div class="signature">
      <span class="signature__square" aria-hidden="true"></span>
      <span class="signature__name">Dulmar</span>
    </div>
    <address class="contact">
      <div class="contact__name">Gergely Tarnavedi</div>
      <div class="contact__title">Managing Director</div>
      <div class="contact__line">g.tarnavedi@dulmar-example.hu</div>
      <div class="contact__line">Mobile: +36 30 555 0192</div>
    </address>
    <div class="card__band">
      <p class="web">www.dulmar-example.hu</p>
    </div>
  </section>

  <div class="note-side">colour options Flexible</div>
  <div class="note-size">3.5x1.75 inch.</div>

</main>
</body>
</html>
```